Quorvantelline.com

I need a site that I can sell dewatering equipment to the construction industry.
Ie, pipes fittings pumps and other such things needed to remove the groundwater on construction sites. Here in Florida, it’s needed almost everywhere seeing we are at sea level.
I want to be able to sell these products on the site and receive

Coded - Design and coding required

1 page

```html
<!DOCTYPE html>
<html lang="en">
<head>
<meta charset="utf-8">
<title>Quorvantelline – Dewatering Equipment</title>
<link href="https://fonts.googleapis.com/css2?family=Lato:wght@300;400;700&display=swap" rel="stylesheet">
<style>
:root{
  --red:#d90718;
  --red-dark:#b5000f;
  --ink:#222222;
  --muted:#666666;
  --light:#f4f4f4;
  --footer:#333333;
  --white:#ffffff;
}
*{box-sizing:border-box;margin:0;padding:0}
html,body{width:1200px;height:3409px;overflow:hidden}
body{position:relative;background:var(--white);font-family:"Lato",Arial,sans-serif;color:var(--ink)}
.abs{position:absolute}
.center{text-align:center}
.btn{position:absolute;display:flex;align-items:center;justify-content:center;border-radius:16px;background:var(--red);color:var(--white);font-size:13px;font-weight:700}

/* header */
.site-header{top:0;left:0;width:1200px;height:127px;background:var(--white)}
.brand{left:0;width:1200px;top:30px;display:flex;flex-direction:column;align-items:center;gap:8px}
.brand-dot{width:44px;height:44px;border-radius:50%;background:var(--red)}
.brand-name{color:var(--red);font-size:22px;font-weight:700}
.header-icons{top:54px;left:962px;display:flex;gap:18px}

/* hero */
.hero{top:127px;left:0;width:1200px;height:555px;overflow:hidden;background:linear-gradient(135deg,#8e8e8e 0%,#cfcfcf 35%,#a35a5d 55%,#bdbdbd 75%,#7a7a7a 100%)}
.hero-shade{inset:0;background:rgba(0,0,0,.28)}
.hero-title{top:222px;left:0;width:1200px;color:var(--white);font-size:38px;font-weight:700}
.hero-text{top:272px;left:420px;width:360px;color:var(--white);font-size:13px;line-height:17px}
.hero-arrow{top:232px;width:34px;height:34px;border:2px solid var(--white);border-radius:50%;display:flex;align-items:center;justify-content:center}
.hero-curve{left:0;bottom:0}
.dots{top:700px;left:576px;display:flex;gap:9px}
.dots span{width:8px;height:8px;border-radius:50%;background:var(--ink)}
.dots span:first-child{background:var(--red)}

/* section titles */
.section-title{left:0;width:1200px;font-size:28px;font-weight:400;letter-spacing:1px}
.slider-nav{display:flex;gap:6px}
.slider-nav span{width:18px;height:18px;border-radius:50%;border:1.5px solid var(--ink);display:flex;align-items:center;justify-content:center}
.slider-nav span.on{background:var(--red);border-color:var(--red)}

/* products */
.product{top:857px;width:221px}
.product-img{height:177px;background:linear-gradient(180deg,#f1f1f1,#dcdcdc)}
.product-name{margin-top:15px;font-size:14px;color:var(--ink);text-align:center}
.product-price{margin-top:5px;font-size:14px;color:var(--red);text-align:center}

/* about band */
.about{top:1246px;left:0;width:1200px;height:477px;background:var(--red)}
.about-img{left:118px;top:70px;width:457px;height:332px;background:linear-gradient(160deg,#6b5f52,#8a7c6a 50%,#5b544c)}
.about-body{left:614px;top:78px;width:470px;color:var(--white)}
.about-body h2{font-size:29px;font-weight:700;line-height:34px;letter-spacing:.5px}
.about-body p{margin-top:22px;font-size:13px;line-height:17px}
.about-body ul{margin-top:22px;list-style:none;font-size:14px;line-height:24px;font-weight:700}
.about-body li::before{content:"";display:inline-block;border-left:7px solid var(--white);border-top:4px solid transparent;border-bottom:4px solid transparent;margin-right:14px}
.btn-white{background:var(--white);color:var(--red)}

/* blogs */
.blog{top:1848px;width:312px;height:323px;background:var(--white);box-shadow:0 0 8px rgba(0,0,0,.12);padding:10px}
.blog-img{position:relative;height:178px}
.blog-tag{position:absolute;top:22px;left:0;background:rgba(0,0,0,.55);color:var(--white);font-size:12px;font-weight:700;padding:2px 6px}
.blog-title{margin-top:12px;font-size:13px;font-weight:700}
.blog-meta{margin-top:4px;display:flex;font-size:13px;color:var(--ink)}
.blog-meta .date{flex:1}
.blog-meta span+span{margin-left:22px}
.blog-text{margin-top:8px;font-size:12px;line-height:16px;color:var(--muted)}
.blog-more{margin-top:6px;font-size:13px;color:var(--muted)}

/* contact */
.contact{top:2321px;left:0;width:598px;height:413px;background:var(--red)}
.contact h2{position:absolute;top:52px;left:0;width:598px;text-align:center;color:var(--white);font-size:30px;font-weight:400}
.contact-rule{top:98px;left:240px;width:118px;height:12px}
.field{position:absolute;background:var(--red-dark);color:var(--white);font-size:13px;font-weight:700;padding:8px 10px}
.map{top:2321px;left:600px;width:600px;height:413px;background:linear-gradient(120deg,#d9d9d9,#a9a9a9 40%,#cfcfcf 70%,#e6e6e6)}

/* newsletter */
.news-title{top:2828px;left:0;width:1200px;font-size:24px;letter-spacing:.5px}
.news-sub{top:2864px;left:0;width:1200px;font-size:13px;color:var(--muted)}
.news-input{top:2900px;left:339px;width:400px;height:30px;background:var(--light);border-radius:15px 0 0 15px;font-size:12px;color:#999;padding:8px 20px}
.news-submit{top:2900px;left:720px;width:132px;height:30px;border-radius:0 15px 15px 0}

/* footer */
.footer{top:3005px;left:0;width:1200px;height:404px;background:var(--footer);color:var(--white)}
.footer-curve{top:0;left:0}
.foot-brand{left:118px;top:112px;display:flex;align-items:center;gap:12px;font-size:22px;font-weight:700}
.foot-brand i{width:38px;height:38px;border:2px solid var(--white);border-radius:50%}
.foot-about{left:118px;top:196px;width:280px;font-size:13px;line-height:17px}
.foot-col h3{font-size:14px;font-weight:700}
.foot-col h3::after{content:"";display:block;width:62px;height:2px;background:var(--white);margin-top:12px}
.foot-col ul{list-style:none;margin-top:20px;font-size:13px;line-height:18px}
.foot-links li::before{content:"•";margin-right:8px}
.foot-address li{display:flex;align-items:flex-start;gap:10px;margin-bottom:1px}
.social{display:flex;flex-direction:column;gap:12px;margin-top:22px}
.social span{width:10px;height:10px;border-radius:50%;background:var(--white)}
.foot-divider{left:118px;top:345px;width:962px;height:1px;background:#777}
.copyright{left:118px;top:369px;font-size:13px}
.cards{left:896px;top:362px;display:flex;gap:10px}
.cards span{width:38px;height:24px;border-radius:3px;background:#e6e6e6}
</style>
</head>
<body>

<header class="site-header abs">
  <div class="brand abs"><span class="brand-dot"></span><span class="brand-name">Quorvantelline</span></div>
  <div class="header-icons abs">
    <svg width="16" height="16" viewBox="0 0 16 16"><path d="M8 14 2 8a3.3 3.3 0 0 1 6-4 3.3 3.3 0 0 1 6 4z" fill="none" stroke="#222" stroke-width="1.6"/></svg>
    <svg width="18" height="16" viewBox="0 0 18 16"><path d="M1 2h3l2 8h9l2-6H5" fill="none" stroke="#222" stroke-width="1.6"/><circle cx="7" cy="14" r="1.4" fill="#222"/><circle cx="14" cy="14" r="1.4" fill="#222"/></svg>
    <svg width="16" height="16" viewBox="0 0 16 16"><circle cx="6.5" cy="6.5" r="4.5" fill="none" stroke="#222" stroke-width="1.6"/><path d="M10 10l5 5" stroke="#222" stroke-width="1.8"/></svg>
    <svg width="18" height="16" viewBox="0 0 18 16"><path d="M1 3h16M1 8h16M1 13h16" stroke="#222" stroke-width="2.2"/></svg>
  </div>
</header>

<section class="hero abs" role="img" aria-label="Close-up photo of red-handled valves and pipe fittings">
  <div class="hero-shade abs"></div>
  <div class="hero-arrow abs" style="left:103px"><svg width="12" height="12" viewBox="0 0 12 12"><path d="M8 1 3 6l5 5" fill="none" stroke="#fff" stroke-width="2"/></svg></div>
  <div class="hero-arrow abs" style="left:1063px"><svg width="12" height="12" viewBox="0 0 12 12"><path d="M4 1l5 5-5 5" fill="none" stroke="#fff" stroke-width="2"/></svg></div>
  <h1 class="hero-title abs center">Quorvantelline Supply</h1>
  <p class="hero-text abs center">Lorem Ipsum is simply dummy text of the matter and typesetting in industry.</p>
  <a class="btn" style="top:323px;left:539px;width:129px;height:27px">Read More</a>
  <svg class="hero-curve abs" width="1200" height="60" viewBox="0 0 1200 60"><path d="M0 0Q600 104 1200 0V60H0z" fill="#fff"/></svg>
</section>
<div class="dots abs"><span></span><span></span><span></span><span></span></div>

<h2 class="section-title abs center" style="top:780px">Feature Product</h2>
<div class="slider-nav abs" style="top:788px;left:1034px">
  <span><svg width="8" height="8" viewBox="0 0 8 8"><path d="M5 1 2 4l3 3" fill="none" stroke="#222" stroke-width="1.5"/></svg></span>
  <span class="on"><svg width="8" height="8" viewBox="0 0 8 8"><path d="M3 1l3 3-3 3" fill="none" stroke="#fff" stroke-width="1.5"/></svg></span>
</div>
<div class="product abs" style="left:118px"><div class="product-img" role="img" aria-label="Steel gate valve assembly"></div><p class="product-name">Product Name 1</p><p class="product-price">$ 100.00</p></div>
<div class="product abs" style="left:361px"><div class="product-img" role="img" aria-label="Pipe manifold with valves"></div><p class="product-name">Product Name 2</p><p class="product-price">$ 100.00</p></div>
<div class="product abs" style="left:609px"><div class="product-img" role="img" aria-label="Yellow gate valve with red handwheel"></div><p class="product-name">Product Name 3</p><p class="product-price">$ 100.00</p></div>
<div class="product abs" style="left:855px"><div class="product-img" role="img" aria-label="Blue flanged valve on yellow pipe"></div><p class="product-name">Product Name 4</p><p class="product-price">$ 100.00</p></div>
<a class="btn" style="top:1139px;left:530px;width:129px;height:27px">View More</a>

<section class="about abs">
  <div class="about-img abs" role="img" aria-label="Construction site excavation with groundwater"></div>
  <div class="about-body abs">
    <h2>Remove the groundwater on construction sites</h2>
    <p>Lorem Ipsum is simply dummy text in of the printing and typesetting industry. Lorem Ipsum has been the industry's standard dummy text ever since the 1500s, when an in unknown printer took a galley of type and scrambled it to make a type specimen book.</p>
    <ul><li>Pumping Services</li><li>Dewatering</li><li>Water Filtration &amp; Treatment</li><li>Drilling</li></ul>
  </div>
  <a class="btn btn-white" style="top:357px;left:616px;width:130px;height:28px">Read More</a>
</section>

<h2 class="section-title abs center" style="top:1784px">Our Blogs</h2>
<div class="slider-nav abs" style="top:1792px;left:1025px">
  <span><svg width="8" height="8" viewBox="0 0 8 8"><path d="M5 1 2 4l3 3" fill="none" stroke="#222" stroke-width="1.5"/></svg></span>
  <span class="on"><svg width="8" height="8" viewBox="0 0 8 8"><path d="M3 1l3 3-3 3" fill="none" stroke="#fff" stroke-width="1.5"/></svg></span>
</div>
<article class="blog abs" style="left:118px">
  <div class="blog-img" role="img" aria-label="Industrial plug valve on a pipe" style="background:linear-gradient(135deg,#8a6a4e,#b08a66 50%,#6d4d3a)"><span class="blog-tag">Mar</span></div>
  <h3 class="blog-title">Industrial plug valve on the pipe</h3>
  <div class="blog-meta"><span class="date">▪ Jun 01, 2018</span><span>♡20</span><span>♡12</span></div>
  <p class="blog-text">Lorem Ipsum is simply dummy text of the matter and typesetting in industry.</p>
  <p class="blog-more">Read More ›</p>
</article>
<article class="blog abs" style="left:446px">
  <div class="blog-img" role="img" aria-label="Hand valve in an industrial plant" style="background:linear-gradient(135deg,#6e6e6e,#b5a39a 45%,#5a5a5a)"><span class="blog-tag">Mar</span></div>
  <h3 class="blog-title">hand valve in industrial plant</h3>
  <div class="blog-meta"><span class="date">▪ Jun 02, 2018</span><span>♡20</span><span>♡12</span></div>
  <p class="blog-text">Lorem Ipsum is simply dummy text of the matter and typesetting in industry.</p>
  <p class="blog-more">Read More ›</p>
</article>
<article class="blog abs" style="left:775px">
  <div class="blog-img" role="img" aria-label="Industrial stainless steel pipework" style="background:linear-gradient(135deg,#7d7d7d,#c9c9c9 45%,#8b5a5a 70%,#6a6a6a)"></div>
  <h3 class="blog-title">industry stainless pipe</h3>
  <div class="blog-meta"><span class="date">▪ Jun 10, 2018</span><span>♡20</span><span>♡12</span></div>
  <p class="blog-text">Lorem Ipsum is simply dummy text of the matter and typesetting in industry.</p>
  <p class="blog-more">Read More ›</p>
</article>
<a class="btn" style="top:2214px;left:530px;width:129px;height:27px">View More</a>

<section class="contact abs">
  <h2>Quick Contact</h2>
  <svg class="contact-rule abs" viewBox="0 0 118 12"><path d="M0 6h46M72 6h46" stroke="#fff" stroke-width="1.5"/><circle cx="59" cy="6" r="5" fill="none" stroke="#fff" stroke-width="1.5"/></svg>
  <div class="field" style="top:127px;left:120px;width:405px;height:36px">Name</div>
  <div class="field" style="top:177px;left:120px;width:198px;height:35px">Phone</div>
  <div class="field" style="top:177px;left:332px;width:193px;height:35px">Email</div>
  <div class="field" style="top:225px;left:120px;width:405px;height:82px">Message</div>
  <a class="btn" style="top:339px;left:120px;width:130px;height:29px;background:#333">View More</a>
</section>
<div class="map abs" role="img" aria-label="Greyscale map of Florida and the Gulf of Mexico"></div>

<h2 class="news-title abs center">Join The Newletter</h2>
<p class="news-sub abs center">Sign up for Our Newsletter</p>
<div class="news-input abs">Email here</div>
<a class="btn news-submit">Submit</a>

<footer class="footer abs">
  <svg class="footer-curve abs" width="1200" height="42" viewBox="0 0 1200 42"><path d="M0 0H1200V41Q600 -41 0 41z" fill="#fff"/></svg>
  <div class="foot-brand abs"><i></i>Quorvantelline</div>
  <p class="foot-about abs">Lorem Ipsum is simply dummy text of the printing and ypesetting industry. has been Lorem Ipsum is simply dummy text the Lorem Ipsum is simply dummy text of the industry's standard. dummy...</p>
  <div class="foot-col abs" style="left:516px;top:125px">
    <h3>Quick Link</h3>
    <ul class="foot-links"><li>Home</li><li>About us</li><li>Product</li><li>Gallery</li><li>Blog</li><li>Contact us</li></ul>
  </div>
  <div class="foot-col abs" style="left:734px;top:125px">
    <h3>Address</h3>
    <ul class="foot-address">
      <li><svg width="10" height="14" viewBox="0 0 10 14"><path d="M5 13S1 8 1 5a4 4 0 0 1 8 0c0 3-4 8-4 8z" fill="#fff"/></svg><span>48 Harbor Lane<br>Florida, USA<br>Zip :1234</span></li>
      <li><svg width="10" height="12" viewBox="0 0 10 12"><path d="M2 1h2l1 3-1.5 1a6 6 0 0 0 3 3L8 7l2 1v2c-5 1-9-4-8-9z" fill="#fff"/></svg><span>+1 555 014 2290</span></li>
      <li><svg width="12" height="10" viewBox="0 0 12 10"><rect width="12" height="9" fill="#fff"/><path d="M0 0l6 5 6-5" fill="none" stroke="#333"/></svg><span>info@quorvantelline.com</span></li>
    </ul>
  </div>
  <div class="foot-col abs" style="left:1007px;top:125px">
    <h3>Follow Us</h3>
    <div class="social"><span></span><span></span><span></span><span></span><span></span></div>
  </div>
  <div class="foot-divider abs"></div>
  <p class="copyright abs">Copyright © 2018 Quorvantelline. All Rights Reserved.</p>
  <div class="cards abs"><span></span><span></span><span></span><span></span></div>
</footer>

</body>
</html>
```